Set up small scale company website

We need a website set up for our educational consultancy - Kelvra Learning. We like the following site and want something similar www.plindaworks.co.uk We can provide the copy and images but need the following:- setting up the overall theme and design - to our requirements on colours and forma- Approximately 4 pages of services offered and with an index pageEtct (yellow and green)And the following pages - as well as a home page:- A contact page linked to our email addresses and registered business address 47 Bramwick Lane, Harwich, Essex, CO14 8RJ- About Us page - An index of services page that links to between 4-6 pages outlining services- A News page that links to updates of latest services, events and activities - easily updated by usOn the homepage we'd like links to twitter and LinkedIn feeds and links to our other blogs and websites
Target Market(s)
Schools, local authoroties and multi-academy trusts
Logo Text
Kelvra Learning
Coding
Coded - Design and coding required
Number of Pages Required
5+ page
Font styles to use
Requirements
Should not have
- No tacky pictures of mortar boards or chalk boards etc.

```html
<!DOCTYPE html>
<html lang="en">
<head>
<meta charset="utf-8">
<title>Kelvra Learning</title>
<link rel="stylesheet" href="https://fonts.googleapis.com/css2?family=Cabin:wght@400;500;600;700&display=swap">
<style>
:root{
  --cream:#fff8c4;
  --card-border:#c9c4a2;
  --card-bg:#ffffff;
  --text:#3a3a3a;
  --link:#1a8ac3;
  --green:#7cb305;
  --footer:#6f6f6f;
  --bar:#3b3b3b;
  --white:#ffffff;
  --map-land:#e6e3dc;
}
*{box-sizing:border-box;margin:0;padding:0}
html,body{width:1200px;height:808px;overflow:hidden}
body{position:relative;background:var(--cream);font-family:"Cabin",Arial,sans-serif;color:var(--text)}
.social-feed{position:absolute;left:0;top:0;width:1200px;height:428px;background:var(--cream)}
.feed-emblem{position:absolute;left:587px;top:23px;width:79px;height:79px;border-radius:8px;background:#e9e1b0}
.feed-nav{position:absolute;left:1048px;top:24px;display:flex;gap:2px}
.feed-nav span{width:43px;height:31px;background:var(--green);display:flex;align-items:center;justify-content:center}
.post{position:absolute;top:121px;width:196px;height:278px;background:var(--card-bg);border:1px solid var(--card-border);padding:16px 7px 0 7px}
.post-body{font-size:13px;line-height:26px;letter-spacing:.2px}
.post-link{display:block;color:var(--link);font-size:13px;line-height:20px;text-decoration:none}
.post-rule{border:0;border-top:1px solid #d8d8d8;margin:16px 7px 18px}
.post-author{color:var(--link);font-size:17.5px;line-height:20px;padding-left:1px}
.post-date{font-size:13.5px;line-height:18px;padding-left:1px}
.site-footer{position:absolute;left:0;top:428px;width:1200px;height:336px;background:var(--footer);color:var(--white)}
.footer-col{position:absolute;top:32px}
.footer-col h3{font-size:17.5px;font-weight:700;margin-bottom:12px;margin-left:-2px}
.footer-col a{display:block;color:var(--white);font-size:14px;line-height:31.5px;text-decoration:none}
.contact-item{display:flex;align-items:center;height:46px;font-size:14px}
.contact-item svg{margin-right:15px}
.location-map{position:absolute;left:650px;top:0;width:488px;height:336px;background:linear-gradient(135deg,#e8e5de 0%,#dfe8cf 45%,#e6e3dc 100%)}
.legal-bar{position:absolute;left:0;top:764px;width:1200px;height:44px;background:var(--bar);color:var(--white);font-size:12.5px;font-weight:600}
.legal-bar span{position:absolute;top:14px}
</style>
</head>
<body>
<section class="social-feed">
  <div class="feed-emblem" role="img" aria-label="Line illustration of a hand holding social media icons"></div>
  <div class="feed-nav">
    <span><svg width="14" height="18" viewBox="0 0 14 18"><path d="M11 2 4 9l7 7" fill="none" stroke="#fff" stroke-width="3"/></svg></span>
    <span><svg width="14" height="18" viewBox="0 0 14 18"><path d="M3 2l7 7-7 7" fill="none" stroke="#fff" stroke-width="3"/></svg></span>
  </div>

  <article class="post" style="left:114px">
    <p class="post-body">Lorem ipsum dolor sit amet, consectetur adipiscing elit, sed do eiusmod tempor incidi-dunt ut labore et dolore magna aliqua.</p>
    <a class="post-link" href="#">http://www.kelvralearn.com</a>
    <hr class="post-rule">
    <div class="post-author">Kelvra Learning</div>
    <div class="post-date">Feb 5th</div>
  </article>
  <article class="post" style="left:390px">
    <p class="post-body">Lorem ipsum dolor sit amet, consectetur adipiscing elit, sed do eiusmod tempor incidi-dunt ut labore et dolore magna aliqua.</p>
    <a class="post-link" href="#">http://www.kelvralearn.com</a>
    <hr class="post-rule">
    <div class="post-author">Kelvra Learning</div>
    <div class="post-date">Feb 5th</div>
  </article>
  <article class="post" style="left:666px">
    <p class="post-body">Lorem ipsum dolor sit amet, consectetur adipiscing elit, sed do eiusmod tempor incidi-dunt ut labore et dolore magna aliqua.</p>
    <a class="post-link" href="#">http://www.kelvralearn.com</a>
    <hr class="post-rule">
    <div class="post-author">Kelvra Learning</div>
    <div class="post-date">Feb 5th</div>
  </article>
  <article class="post" style="left:942px">
    <p class="post-body">Lorem ipsum dolor sit amet, consectetur adipiscing elit, sed do eiusmod tempor incidi-dunt ut labore et dolore magna aliqua.</p>
    <a class="post-link" href="#">http://www.kelvralearn.com</a>
    <hr class="post-rule">
    <div class="post-author">Kelvra Learning</div>
    <div class="post-date">Feb 5th</div>
  </article>
</section>

<footer class="site-footer">
  <nav class="footer-col" style="left:118px">
    <h3>Menu</h3>
    <a href="#">Home</a><a href="#">Services</a><a href="#">News</a><a href="#">About Us</a><a href="#">Contact</a>
  </nav>
  <nav class="footer-col" style="left:236px">
    <h3>Services</h3>
    <a href="#">Finance</a><a href="#">Personnel</a><a href="#">Facilitis</a><a href="#">Academy Conversion</a><a href="#">Staff Solution</a><a href="#">Auditing</a>
  </nav>
  <div class="footer-col" style="left:408px">
    <h3>Contact</h3>
    <div class="contact-item">
      <svg width="28" height="28" viewBox="0 0 28 28"><circle cx="14" cy="14" r="14" fill="#fff"/><path d="M9 7c1 0 2 2 3 4 0 1-1 1.5-1 2 1 2 2 3 4 4 .5 0 1-1 2-1 2 1 4 2 4 3 0 2-2 3-3 3-6 0-12-6-12-12 0-1 1-3 3-3z" fill="var(--footer)"/></svg>
      <span>68 412 305</span>
    </div>
    <div class="contact-item" style="margin-top:4px">
      <svg width="28" height="28" viewBox="0 0 28 28"><circle cx="14" cy="14" r="14" fill="#fff"/><rect x="7" y="9" width="14" height="10" rx="1.5" fill="var(--footer)"/><path d="M7.5 10l6.5 5 6.5-5" fill="none" stroke="#fff" stroke-width="1.3"/></svg>
      <span>info@kelvra.com</span>
    </div>
    <div class="contact-item" style="margin-top:4px">
      <svg width="28" height="28" viewBox="0 0 28 28"><circle cx="14" cy="14" r="14" fill="#fff"/><rect x="10" y="7" width="8" height="5" fill="var(--footer)"/><rect x="7" y="11" width="14" height="7" rx="1.5" fill="var(--footer)"/><rect x="10" y="16" width="8" height="6" fill="var(--footer)" stroke="#fff" stroke-width="1"/></svg>
      <span>68 412 305</span>
    </div>
  </div>
  <div class="location-map" role="img" aria-label="Street map showing the office location"></div>
</footer>

<div class="legal-bar">
  <span style="left:114px">Copyright © 2019 Kelvra Learning</span>
  <span style="left:745px">Copyright Information</span>
  <span style="left:908px">Terms and Condition</span>
  <span style="left:1063px">Privacy Policy</span>
</div>
</body>
</html>
```